Design a modern, classy & professional business card for an online real estate agency, specializing in medium-luxury properties in Thailand and later in Singapore and UK.

Possible design ideas so far: (not essential)

- curved corner(s) to the card, white on front & turquoise on back or visa versa.

- front of card - clear and simple, company name in metallic grey/monochrome, logo graphic & company name on front in spot UV or embossed/debossed effect.

- back of card - large, close-cropped, 'ghost' patterns of the C-shaped curves of logo, or company name repeated on back of card in spot UV.

Target Market(s)

- young to middle-aged professionals mainly (but ideally should design should suit all)

- UK, US,EU,AUS & ASIAN mainly (but ideally should design should suit all countries)

Industry/Entity Type

Real Estate

Requirements
Must have
• THEME:
- Luxurious & Modern
- Clean & striking
- Unique & creative

INFO:
- Logo & company name on front
- Contact details on back:

Tobias Lindqvar
Managing Director

www.velmoraestates.example
www.velmoraestates-uk.example

Tel: 084-273-6190
email: tobias@velmoraestates.example

(contact details can be displayed in any order as suites design.)

Nice to have
• - curved corner(s) to the card, white on front & turquoise on back or visa versa.

Should not have
• - No generic images of properties, palm trees/coconut trees etc.

- No other other bold colors, except for main turquoise, grey, metallic white & black theme.

- No obvious business card templates

```html
<!DOCTYPE html>
<html lang="en">
<head>
<meta charset="utf-8">
<title>Velmora Estates – Business Card Back</title>
<link rel="stylesheet" href="https://fonts.googleapis.com/css2?family=Montserrat:wght@300;400;600;700&display=swap">
<style>
  :root {
    --page-bg: #ffffff;
    --card-turquoise: #1fb3ad;
    --card-turquoise-light: #2cc6c0;
    --card-turquoise-dark: #18a29c;
    --ink-white: #ffffff;
    --caption-grey: #8a8a8a;
    --caption-grey-strong: #6f6f6f;
  }
  * { margin: 0; padding: 0; box-sizing: border-box; }
  html, body {
    width: 1200px;
    height: 1000px;
    overflow: hidden;
    background: var(--page-bg);
    font-family: "Montserrat", Arial, sans-serif;
  }
  .canvas {
    position: relative;
    width: 1200px;
    height: 1000px;
  }
  .card-back {
    position: absolute;
    left: 220px;
    top: 190px;
    width: 760px;
    height: 498px;
    border-radius: 44px;
    background: var(--card-turquoise);
    overflow: hidden;
    color: var(--ink-white);
  }
  .ghost-pattern {
    position: absolute;
    left: 0;
    top: 0;
    width: 440px;
    height: 330px;
  }
  .contact-block {
    position: absolute;
    right: 80px;
    top: 150px;
    text-align: right;
  }
  .person-name {
    font-weight: 700;
    font-size: 21px;
    letter-spacing: 0.24em;
    text-transform: uppercase;
    margin-right: -0.24em;
  }
  .person-title {
    font-weight: 300;
    font-size: 16px;
    letter-spacing: 0.26em;
    text-transform: uppercase;
    margin-top: 6px;
    margin-right: -0.26em;
  }
  .contact-lines {
    margin-top: 58px;
    list-style: none;
    font-size: 19px;
    line-height: 1.3;
  }
  .contact-phone,
  .contact-email { font-weight: 300; }
  .contact-web { font-weight: 700; }
  .sheet-caption {
    position: absolute;
    left: 0;
    width: 1200px;
    top: 898px;
    text-align: center;
    font-size: 17px;
    font-weight: 400;
    letter-spacing: 0.2em;
    color: var(--caption-grey);
    text-transform: uppercase;
  }
  .sheet-caption strong {
    font-weight: 600;
    color: var(--caption-grey-strong);
  }
</style>
</head>
<body>
<main class="canvas">
  <section class="card-back" aria-label="Velmora Estates business card, back">
    <svg class="ghost-pattern" viewBox="0 0 440 330" role="img" aria-label="Faint spot UV curve pattern area">
      <defs>
        <radialGradient id="ghostGlow" cx="0.45" cy="0.4" r="0.6">
          <stop offset="0" stop-color="var(--card-turquoise-light)" stop-opacity="0.7"/>
          <stop offset="1" stop-color="var(--card-turquoise)" stop-opacity="0"/>
        </radialGradient>
      </defs>
      <rect width="440" height="330" fill="url(#ghostGlow)"/>
    </svg>

    <div class="contact-block">
      <h1 class="person-name">Tobias Lindqvar</h1>
      <p class="person-title">Managing Director</p>
      <ul class="contact-lines">
        <li class="contact-phone">T.084-273-6190</li>
        <li class="contact-email">tobias@velmoraestates.example</li>
        <li class="contact-web">www.velmoraestates.example</li>
        <li class="contact-web">www.velmoraestates-uk.example</li>
      </ul>
    </div>
  </section>

  <p class="sheet-caption"><strong>Back</strong> 84mm x 55mm spot UV print “C” curve pattern</p>
</main>
</body>
</html>
```